High-Class Professional Letterhead for a solo doctor's practice.

Please create a letterhead design that includes my logo, and options of my light blue/black color scheme and black and gold so I can choose between the two. I would like my Contact information on the top or bottom of the letterhead somewhere:
Delia Forsk, M.D.
Hand and Upper Extremity Surgeon
4382 NW 58th Lane, Suite 307
Corvell, GA 30498
Phone: (470) 316-8842
Fax: (800) 629-4087
www.dforskgrip.example

Also on the bottom of the letterhead, there should be 2 different versions:
one that is blank, and one that has a signature spot on the bottom so I can sign:
Delia Forsk, M.D.
Board Certified Orthopaedic Hand Surgeon

I am going for classy/professional. I want other doctors and or lawyers to look at my letterhead and want to work with me. Again, professional, classy, clean. I do like black and gold but I could see what the blue like my other business card looks like too. Please do what most people do for letterheads--I'm not sure if the signature line should be on there? Or should be blank? I have no clue

Target Market(s)

Doctors and Lawyers

Industry/Entity Type

Medicine

Colors
0054AA
0677BA
7BADD7
CADEEF
E8F1F8

Requirements
Must have
• High class, professional, appealing

```html
<!DOCTYPE html>
<html lang="en">
<head>
<meta charset="utf-8">
<title>Delia Forsk, M.D. — Letterhead</title>
<link href="https://fonts.googleapis.com/css2?family=Lato:wght@400;700&family=Montserrat:wght@400;700&display=swap" rel="stylesheet">
<style>
  :root {
    --canvas: #e6e6e6;
    --paper: #ffffff;
    --ink: #000000;
    --gold: #cdb07a;
    --gold-deep: #b8965a;
    --heading: #222222;
    --body: #8c8c8c;
    --muted: #6f6f6f;
  }
  * { box-sizing: border-box; margin: 0; padding: 0; }
  html, body { width: 1200px; height: 1033px; overflow: hidden; background: var(--canvas); }
  .letterhead {
    position: absolute; left: 241px; top: 16px;
    width: 718px; height: 1000px;
    background: var(--paper);
    box-shadow: 0 6px 24px rgba(0,0,0,.12);
    font-family: "Lato", sans-serif;
  }
  .header-band { position: absolute; left: 0; top: 0; width: 718px; height: 200px; }
  .practice-name {
    position: absolute; left: 48px; top: 70px;
    font-family: "Lato", sans-serif; font-weight: 700;
    font-size: 20px; letter-spacing: 1px; color: var(--gold);
  }
  .contact {
    position: absolute; right: 49px; top: 88px;
    text-align: right; font-family: "Montserrat", sans-serif; font-style: normal;
    color: var(--ink); font-size: 10.5px; line-height: 15.5px;
  }
  .contact__name { font-weight: 700; font-size: 13px; line-height: 16px; }
  .contact__title { margin-bottom: 3px; }
  .contact__label { color: var(--gold-deep); font-weight: 700; }
  .contact__web { margin-bottom: 4px; }
  .greeting {
    position: absolute; left: 66px; top: 280px;
    font-size: 15.5px; font-weight: 700; color: var(--heading);
  }
  .date {
    position: absolute; right: 50px; top: 279px;
    font-size: 15.5px; color: var(--muted);
  }
  .body-copy {
    position: absolute; left: 64px; top: 343px; width: 606px;
    font-size: 13.2px; line-height: 26.2px; color: var(--body);
    text-align: justify; hyphens: auto; -webkit-hyphens: auto;
  }
  .body-copy .new-paragraph { margin-top: 26px; }
  .signature-area {
    position: absolute; left: 55px; top: 822px; width: 270px; height: 40px;
    background: linear-gradient(90deg, rgba(0,0,0,.04), rgba(0,0,0,.09), rgba(0,0,0,.04));
    border-radius: 3px;
  }
  .signature-title {
    position: absolute; left: 66px; top: 869px;
    font-size: 12.5px; color: var(--ink);
  }
</style>
</head>
<body>
  <main class="letterhead">
    <svg class="header-band" viewBox="0 0 718 200" aria-hidden="true">
      <path fill="var(--ink)" d="M0 0 H718 V40 Q420 60 300 120 Q180 178 0 176 Z"/>
      <path fill="none" stroke="var(--gold)" stroke-width="3" d="M718 52 Q430 70 310 130 Q190 188 0 186"/>
    </svg>

    <div class="practice-name">Forsk Surgical</div>

    <address class="contact">
      <div class="contact__name">Delia Forsk, M.D.</div>
      <div class="contact__title">Hand and Upper Extremity Surgeon</div>
      <div><span class="contact__label">P:</span> (470) 316-8842</div>
      <div><span class="contact__label">F:</span> (800) 629-4087</div>
      <div class="contact__web">www.dforskgrip.example</div>
      <div>4382 NW 58th Lane, Suite 307</div>
      <div>Corvell, GA 30498</div>
    </address>

    <p class="greeting">Dear Mr. Halvorsen,</p>
    <p class="date">Dec 04, 2023</p>

    <section class="body-copy">
      <p>Lorem ipsum dolor sit amet, consectetur adipiscing elit, sed do eiusmod tempor incididunt ut labore et dolore magna aliqua. Ut enim ad minim veniam, quis nostrud exercitation ullamco laboris nisi ut aliquip ex ea commodo consequat. Duis aute irure dolor in reprehenderit in voluptate velit esse cillum dolore eu fugiat nulla pariatur. Excepteur sint occaecat cupidatat non proident, sunt in culpa qui officia dese&shy;runt mollit anim id est laborum.</p>
      <p class="new-paragraph">Lorem ipsum dolor sit amet, consectetur adipiscing elit, sed do eiusmod tempor incididunt ut labore et dolore magna aliqua. Ut enim ad minim veniam, quis nostrud exercitation ullamco laboris nisi ut aliquip ex ea commodo consequat. Duis aute irure dolor in reprehenderit in voluptate velit esse cillum dolore eu fugiat nulla pariatur. Excepteur sint occaecat cupidatat non proident, sunt in culpa qui officia dese&shy;runt mollit anim id est laborum.Lorem ipsum dolor sit amet, consectetur adipiscing elit, sed do eiusmod tempor incididunt ut labore et dolore magna aliqua. Ut enim ad minim veniam, quis nostrud exercita&shy;tion consectetur adipiscing elit, sed do eiusmod tempor incididunt ut labore et dolore magna aliqua. Ut enim ad minim veniam, quis nostrud exercitation.</p>
      <p>&nbsp;consectetur adipiscing elit, sed do eiusmod tempor incididunt ut labore et dolore magna aliqua. Ut enim ad minim veniam, quis nostrud exercitation consectetur adipiscing elit, sed do eiusmod tempor incididunt ut labore et dolore magna aliqua.</p>
    </section>

    <div class="signature-area" role="img" aria-label="Handwritten signature of Delia Forsk, M.D."></div>
    <p class="signature-title">Board Certified Orthopaedic Hand Surgeon</p>
  </main>
</body>
</html>
```